Thank you for shopping with us business card

We would like a thank you card for our rebranded business. We used to be "Brindle Goods" but are now "Marlow Finds. Old thank you card and new logo will be attached for reference. New thank you card does not have to be same design as old thank you card, but please use new logo.
Shopmart URL is now marlowfinds.shopmart.example
Instagram is @Marlow_Finds
Email is marlowfinds@mailbox.example
Thank you!

Contact Information for Business Card

Shopmart site, email, Instagram

```html
<!DOCTYPE html>
<html lang="en">
<head>
<meta charset="utf-8">
<title>Marlow Finds – Thank You Card</title>
<link href="https://fonts.googleapis.com/css2?family=Lato:wght@400;900&family=Montserrat:wght@600&display=swap" rel="stylesheet">
<style>
  :root {
    --backdrop: #6b6b6b;
    --ink: #000000;
    --paper: #ffffff;
  }
  * { margin: 0; padding: 0; box-sizing: border-box; }
  html, body { width: 1200px; height: 1200px; overflow: hidden; }
  body { background: var(--backdrop); position: relative; font-family: "Lato", Arial, sans-serif; }

  .card { position: absolute; top: 200px; width: 468px; height: 821px; overflow: hidden; }

  .card-front { left: 113px; background: var(--ink); color: var(--paper); }
  .front-mark {
    position: absolute; left: 50%; top: 430px; width: 170px; height: 170px;
    transform: translate(-50%, -50%); border-radius: 50%; background: var(--paper);
  }
  .front-name {
    position: absolute; left: 0; right: 0; top: 705px; text-align: center;
    font-family: "Montserrat", Arial, sans-serif; font-weight: 600; font-size: 36px;
    letter-spacing: 0.5px; text-transform: uppercase;
  }

  .card-back { left: 623px; background: var(--paper); color: var(--ink); }
  .back-hex { position: absolute; inset: 0; }
  .thanks-title {
    position: absolute; left: 0; right: 0; top: 38px; text-align: center;
    font-weight: 900; font-size: 64px; line-height: 1; letter-spacing: -0.5px;
  }
  .thanks-sub {
    position: absolute; left: 0; right: 0; top: 102px; text-align: center;
    font-weight: 400; font-size: 33px; line-height: 1;
  }
  .thanks-message {
    position: absolute; left: 0; right: 0; top: 318px; text-align: center;
    color: var(--paper); font-size: 24.5px; line-height: 33px;
  }
  .thanks-message p + p { margin-top: 28px; }
  .back-name {
    position: absolute; left: 0; right: 0; top: 590px; text-align: center;
    color: var(--paper); font-size: 24px; font-weight: 900;
  }
  .contact-list { position: absolute; left: 58px; top: 710px; list-style: none; }
  .contact-item { display: flex; align-items: center; height: 31.5px; font-size: 23px; }
  .contact-icon { width: 20px; height: 20px; margin-right: 16px; flex: none; }
  .icon-square { background: var(--ink); }
  .icon-circle { border: 2.5px solid var(--ink); border-radius: 50%; }
</style>
</head>
<body>
  <section class="card card-front">
    <div class="front-mark" aria-hidden="true"></div>
    <h1 class="front-name">Marlow Finds</h1>
  </section>

  <section class="card card-back">
    <svg class="back-hex" viewBox="0 0 468 821" aria-hidden="true">
      <polygon points="234,156 468,287 468,560 234,692 0,560 0,287" fill="var(--ink)"/>
    </svg>
    <h2 class="thanks-title">THANK YOU</h2>
    <div class="thanks-sub">FOR YOUR PURCHASE</div>
    <div class="thanks-message">
      <p>Your purchase<br>made my day and I hope<br>this package brighten yours.</p>
      <p>Please come back<br>and leave a review!</p>
    </div>
    <div class="back-name">Marlow Finds</div>
    <ul class="contact-list">
      <li class="contact-item"><span class="contact-icon icon-square"></span>marlowfinds.shopmart.example</li>
      <li class="contact-item"><span class="contact-icon icon-circle"></span>@Marlow_Finds</li>
      <li class="contact-item">
        <svg class="contact-icon" viewBox="0 0 20 20" aria-hidden="true">
          <rect x="1" y="4" width="18" height="13" fill="var(--ink)"/>
          <polyline points="1.5,4.5 10,11 18.5,4.5" fill="none" stroke="var(--paper)" stroke-width="1.6"/>
        </svg>marlowfinds@mailbox.example</li>
    </ul>
  </section>
</body>
</html>
```